Design a large parking banner – mandatory ticket validation in the shop

Banner Size:
548 cm (width) x 154 cm (height)
Note: The banner will be placed in a metal frame at our parking lot entrance, fully visible to every incoming truck driver. The message must be easy to read from a distance.
Goal of the Banner:
To inform all truck drivers that they must validate their entry ticket inside the shop, even if they are parking for a short time.
The message must be displayed in multiple languages for international drivers.
Mandatory Content:
Main message – in multiple languages (clearly separated or stacked):
Dutch (NL): Vergeet je ticket niet te valideren in de shop – verplicht, ook bij kort parkeren!
French (FR): N'oubliez pas de valider votre ticket à la boutique – obligatoire, même pour un court arrêt !
English (EN): Don't forget to validate your entry ticket in the shop – mandatory, even for short stops!
German (DE): Vergessen Sie nicht, Ihr Einfahrticket im Shop zu entwerten – Pflicht, auch bei kurzem Parken!
Polish (PL): Nie zapomnij zatwierdzić biletu w sklepie – obowiązkowe, nawet przy krótkim postoju!
Romanian (RO): Nu uitați să validați biletul în magazin – obligatoriu, chiar și pentru opriri scurte!
You can include more languages if space allows, but these are essential.
Opening Hours Block (in one section below):
Shop Opening Hours
Mon – Fri: 05:30 – 22:00
Sat & Sun: 08:00 – 22:00
Style & Branding:
The design must match the visual identity of Haulpoint 41Ter
Please refer to the attached photos of existing parking signage for guidance on colors, typography, and layout style
Our logo (attached) must be clearly visible and professionally integrated
Feel free to use icons or pictograms to visually support the message (e.g., ticket, truck, arrow)
Readability is key – large, bold text and high contrast colors that are visible from a distance
Target Audience:
International truck drivers – people who need fast, clear communication. Not everyone speaks the local language, so visual clarity and multilingual messaging are critical.
File Requirements:
Print-ready file (PDF or EPS) – 300 dpi at 1:10 scale
Include 5 cm bleed on all sides
Provide open source files if possible (AI or PSD)

```html
<!DOCTYPE html>
<html lang="en">
<head>
<meta charset="utf-8">
<title>Haulpoint 41Ter – Ticket Validation Banner</title>
<link rel="stylesheet" href="https://fonts.googleapis.com/css2?family=Montserrat:wght@300;400;500;600;700&display=swap">
<style>
  :root {
    --navy: #1f2149;
    --sky-blue: #1a86c8;
    --signal-red: #d0121b;
    --white: #ffffff;
    --stage: #e8eaef;
    --photo-light: #e4e6ea;
    --photo-mid: #b9c0cc;
  }
  * { margin: 0; padding: 0; box-sizing: border-box; }
  html, body {
    width: 1200px; height: 779px; overflow: hidden;
    background: var(--stage);
    font-family: "Montserrat", sans-serif;
  }
  .banner {
    position: absolute; left: 20px; top: 186px;
    width: 1160px; height: 407px;
    background: var(--navy);
    overflow: hidden;
    color: var(--white);
  }
  .banner-shapes { position: absolute; inset: 0; }

  .headline-block { position: absolute; left: 24px; top: 40px; white-space: nowrap; }
  .kicker { font-size: 25px; font-weight: 500; line-height: 1; letter-spacing: -0.2px; }
  .headline {
    margin-top: 10px; font-size: 46px; font-weight: 500;
    line-height: 54px; letter-spacing: -0.8px;
  }
  .headline .mark { background: var(--sky-blue); padding: 0 6px; margin-left: -2px; }

  .hours-block { position: absolute; left: 27px; top: 258px; white-space: nowrap; }
  .hours-title { font-size: 19px; font-weight: 600; line-height: 29px; }
  .hours-title .mark { background: var(--signal-red); padding: 0 3px; }
  .hours-list { margin-top: 6px; font-size: 19px; font-weight: 300; line-height: 27px; letter-spacing: -0.2px; }

  .notice-block { position: absolute; left: 456px; top: 34px; width: 410px; }
  .notice-title {
    font-size: 22px; font-weight: 700; letter-spacing: -0.5px;
    line-height: 30px; margin-left: 8px; white-space: nowrap;
  }
  .notice-title .mark { background: var(--sky-blue); padding: 0 4px; }
  .notice-list { list-style: none; margin-top: 12px; }
  .notice-item {
    display: flex; align-items: flex-start; gap: 12px;
    height: 52.5px; font-size: 12px; font-weight: 300;
    line-height: 1.55; letter-spacing: -0.2px;
  }
  .notice-text { width: 378px; }
  .notice-hash { font-size: 26px; font-weight: 300; line-height: 1; width: 18px; flex: none; margin-top: 2px; }

  .brand-name {
    position: absolute; left: 945px; top: 312px; width: 200px;
    font-size: 22px; font-weight: 700; color: var(--navy);
    text-align: center; line-height: 1; white-space: nowrap;
  }
</style>
</head>
<body>
  <section class="banner">
    <svg class="banner-shapes" width="1160" height="407" viewBox="0 0 1160 407">
      <defs>
        <linearGradient id="shop-tones" x1="0" y1="0" x2="1" y2="1">
          <stop offset="0" stop-color="#e4e6ea"/>
          <stop offset="1" stop-color="#b9c0cc"/>
        </linearGradient>
      </defs>
      <polygon points="0,152 489,407 0,407" fill="#1a86c8"/>
      <polygon role="img" aria-label="Photo of the shop interior with stocked shelves and a hanging parking zone sign"
               points="851,0 1160,0 1160,407 851,407 986,208" fill="url(#shop-tones)"/>
      <polyline points="834,0 980,208 834,407" fill="none" stroke="#d0121b" stroke-width="2"/>
    </svg>

    <div class="headline-block">
      <p class="kicker">SHORT STOP OR LONG STAY</p>
      <h1 class="headline"><span class="mark">TICKET MUST</span> BE<br>VALIDATED<br>&nbsp;IN THE SHOP.</h1>
    </div>

    <div class="hours-block">
      <p class="hours-title">SHOP <span class="mark">OPENING</span><br>HOURS.</p>
      <p class="hours-list">Mon – Fri: 05:30 – 22:00<br>Sat &amp; Sun: 08:00 – 22:00</p>
    </div>

    <div class="notice-block">
      <h2 class="notice-title">PLEASE <span class="mark">REVIEW CAREFULLY</span></h2>
      <ul class="notice-list">
        <li class="notice-item"><span class="notice-hash">#</span><span class="notice-text">English (EN): Don't forget to validate your entry ticket in the shop – mandatory, even for short stops!</span></li>
        <li class="notice-item"><span class="notice-hash">#</span><span class="notice-text">French (FR): N'oubliez pas de valider votre ticket à la boutique – obligatoire, même pour un court arrêt !</span></li>
        <li class="notice-item"><span class="notice-hash">#</span><span class="notice-text">Dutch (NL): Vergeet je ticket niet te valideren in de shop – verplicht, ook bij kort parkeren!</span></li>
        <li class="notice-item"><span class="notice-hash">#</span><span class="notice-text">German (DE): Vergessen Sie nicht, Ihr Einfahrticket im Shop zu entwerten – Pflicht, auch bei kurzem Parken!</span></li>
        <li class="notice-item"><span class="notice-hash">#</span><span class="notice-text">Polish (PL): Nie zapomnij zatwierdzić biletu w sklepie – obowiązkowe, nawet przy krótkim postoju!</span></li>
        <li class="notice-item"><span class="notice-hash">#</span><span class="notice-text">Romanian (RO): Nu uitați să validați biletul în magazin – obligatoriu, chiar și pentru opriri scurte!</span></li>
      </ul>
    </div>

    <p class="brand-name">Haulpoint 41Ter</p>
  </section>
</body>
</html>
```